Etiketten-Design für Honiggläser
Die Zusammenarbeit mit Jorek war sehr unkompliziert. Änderungswünsche wurden prompt umgesetzt und die Beratung war hervorragend! Besten Dank für das tolle Etikett!
Zielgruppe
Wir sind Imker und benötigen Etiketten für Honiggläser.
Aufgabenstellung
Siehe Anlage. Es sollen keine Fotos verwendet werden. Grafiken sind in Ordnung.
Etiketten-Design für Honigglas Etiketten-Design für Honigglas"
Format: Etikett für 250-gr.-Honigglas (TO ∅ 63 mm). Standardmaßgrösse 165 × 40 mm Design: schlicht, hochwertig, modern, edel/royal, unkonventionelles Design (weg von Bienen, Waben, Landschaften usw.), dunkle Farbtöne in Kontrast zu heller Schrift, die beiden Textbausteine 'Los Nr. ' sowi..
Attraktives Etiketten-Design für Honig Attraktives Etiketten-Design für Honig"
Wir verkaufen zur Zeit vor allem Waldhonig, streben aber auch einen Blütenhonig an. Das Etikett soll daher entweder den Wald wiederspiegeln oder aber neutral sein, so dass der Schriftzug Waldhonig oder Blütenhonig jeweils eingesetzt werden kann. Wichtig ist mir der Ortszusatz 'aus dem Glottertal..
Etiketten-Design für Produkte eines Familienbetriebs mit Imkerei und Hühnerhaltung Etiketten-Design für Produkte eines Familienbetriebs mit Imkerei und Hühnerhaltung"
1. Zentrale, auf allen Etiketten wiederkehrende Elemente: - Unser Riegelhaus (stilisiert) (Bild beiliegend) - Das Wort 'Moosrain' (Anmerkung: ohne Anführungszeichen) - die zentralen Elemente sollen die Produkte nicht überragen. 2. Dezente Adresse: - Familie Drabbel, Lindacker, CH-9612 Fallmatt 3...
Etiketten-Design für Kurkuma-Honig Etiketten-Design für Kurkuma-Honig"
Etikett für 500g // Stanze eckig (210x35mm), Druckdatei entsprechend Vorgaben https://klebeprofi-muster.de/faq/ Vorgaben für das Ackerwert Logo im Anhang Vorgaben für EG Öko Logo : https://oeko-siegel-beispiel.eu/downloads/logo_de Pflichtangaben auf dem Etikett: Gewicht, Adresse siehe Beispiel..
Etiketten-Design für Blütenhonig und Waldhonig gesucht Etiketten-Design für Blütenhonig und Waldhonig gesucht"
Zwei verschiedene Etiketten-Desings 1 x Blütenhonig sowie 1 x Waldhonig für unterschiedliche Honigglasgrößen (500 g und 250 g) Die Maße für die Etiketten wären: Für 500-Gramm-Glas 210 mm x 45 mm für's 250-Gramm-Glas 180 mm x 38 mm. Wir sind auch offen für neue Vorschläge bezüglich ..

```html
<!DOCTYPE html>
<html lang="de">
<head>
<meta charset="utf-8">
<title>Bayerischer Bienenhonig – Etiketten</title>
<link rel="stylesheet" href="https://fonts.googleapis.com/css2?family=Oswald:wght@500&family=Great+Vibes&family=Roboto+Condensed:wght@300;400;700&display=swap">
<style>
  :root {
    --bg: #f1f1f1;
    --sommer: #d5683f;
    --sommer-deep: #b9542f;
    --frueh: #4f93ad;
    --frueh-deep: #3c7b93;
    --spaet: #4d7f6c;
    --spaet-deep: #3b6757;
    --ink: #232323;
    --paper: #ffffff;
  }
  * { box-sizing: border-box; margin: 0; padding: 0; }
  html, body { width: 1200px; height: 615px; overflow: hidden; }
  body {
    background: var(--bg);
    font-family: "Roboto Condensed", Arial, sans-serif;
    position: relative;
  }
  .label-set {
    position: absolute;
    top: 103px;
    width: 304px;
    height: 340px;
  }
  .label-set--sommer { left: 93px;  --theme: var(--sommer); --theme-deep: var(--sommer-deep); }
  .label-set--frueh  { left: 461px; --theme: var(--frueh);  --theme-deep: var(--frueh-deep); }
  .label-set--spaet  { left: 827px; --theme: var(--spaet);  --theme-deep: var(--spaet-deep); }

  /* vertical info strip */
  .info-strip {
    position: absolute;
    left: 117px;
    top: 0;
    width: 70px;
    height: 210px;
    background: var(--theme);
    color: var(--paper);
    text-align: center;
    padding-top: 14px;
  }
  .info-strip__mark {
    width: 14px; height: 14px;
    border: 1.5px solid var(--paper);
    border-radius: 50%;
    margin: 0 auto 12px;
  }
  .info-strip__note,
  .info-strip__fact {
    font-size: 3.6px;
    line-height: 1.45;
    font-weight: 300;
    padding: 0 5px;
    opacity: .9;
  }
  .info-strip__fact { margin-top: 6px; }
  .info-strip__fact strong { font-weight: 700; display: block; }
  .info-strip__lot {
    width: 52px; height: 13px;
    border: 1px solid var(--paper);
    background: var(--paper);
    box-shadow: inset 0 0 0 1px var(--theme-deep);
    margin: 10px auto 0;
  }
  .info-strip__weight {
    font-family: "Oswald", Arial, sans-serif;
    font-weight: 500;
    font-size: 12px;
    margin-top: 8px;
  }
  .info-strip__rule {
    width: 16px; height: 1px;
    background: var(--paper);
    margin: 5px auto 6px;
    opacity: .8;
  }
  .info-strip__address {
    font-size: 3.6px;
    line-height: 1.45;
    font-weight: 300;
    font-style: normal;
  }
  .info-strip__address strong { font-weight: 700; }

  /* horizontal front band */
  .front-band {
    position: absolute;
    left: 0;
    top: 210px;
    width: 304px;
    height: 129px;
    background: var(--theme);
  }
  .front-band__pattern {
    position: absolute; inset: 0;
    background: linear-gradient(135deg, var(--theme) 0%, var(--theme-deep) 50%, var(--theme) 100%);
  }
  .name-plate {
    position: absolute;
    left: 77px;
    top: 17px;
    width: 150px;
    height: 92px;
    background: var(--paper);
    padding: 3px;
  }
  .name-plate__frame {
    width: 100%; height: 100%;
    border: 1px solid var(--theme);
    text-align: center;
    padding-top: 7px;
    position: relative;
  }
  .name-plate__mark {
    width: 9px; height: 9px;
    background: var(--ink);
    border-radius: 50%;
    margin: 0 auto 3px;
  }
  .name-plate__region {
    font-size: 6.5px;
    letter-spacing: 3px;
    color: var(--ink);
    padding-left: 3px;
  }
  .name-plate__title {
    font-family: "Oswald", Arial, sans-serif;
    font-weight: 500;
    font-size: 23px;
    line-height: 1;
    color: var(--theme);
    letter-spacing: -.2px;
    margin-top: 2px;
  }
  .name-plate__season {
    font-family: "Great Vibes", cursive;
    font-size: 23px;
    line-height: 1;
    color: var(--ink);
    margin-top: -9px;
    position: relative;
  }
  .name-plate__kind {
    font-size: 6.5px;
    color: #555;
    font-weight: 300;
    margin-top: -1px;
  }
</style>
</head>
<body>

<section class="label-set label-set--sommer">
  <div class="info-strip">
    <div class="info-strip__mark"></div>
    <p class="info-strip__note">Bienenhonig kristallisiert bei längerer Lagerung. Durch Erwärmen im Wasserbad bei 40° C kann Honig ohne Schaden wieder verflüssigt werden.</p>
    <p class="info-strip__fact"><strong>Lagerhinweis:</strong>Kühl, dunkel und trocken lagern.</p>
    <p class="info-strip__fact"><strong>Ursprungsland:</strong>Deutschland</p>
    <div class="info-strip__lot"></div>
    <p class="info-strip__weight">500g</p>
    <div class="info-strip__rule"></div>
    <address class="info-strip__address"><strong>Imkerei Brenntal</strong><br>Auenweg 12<br>85399 Kleinfeld<br>info@imkerei-brenntal.de</address>
  </div>
  <div class="front-band">
    <div class="front-band__pattern" role="img" aria-label="Linienillustration großer Sonnenblumenblüten auf Orange"></div>
    <div class="name-plate"><div class="name-plate__frame">
      <div class="name-plate__mark"></div>
      <p class="name-plate__region">BAYERISCHER</p>
      <h2 class="name-plate__title">BIENENHONIG</h2>
      <p class="name-plate__season">Sommertracht</p>
      <p class="name-plate__kind">Blütenhonig &amp; Honigtau</p>
    </div></div>
  </div>
</section>

<section class="label-set label-set--frueh">
  <div class="info-strip">
    <div class="info-strip__mark"></div>
    <p class="info-strip__note">Bienenhonig kristallisiert bei längerer Lagerung. Durch Erwärmen im Wasserbad bei 40° C kann Honig ohne Schaden wieder verflüssigt werden.</p>
    <p class="info-strip__fact"><strong>Lagerhinweis:</strong>Kühl, dunkel und trocken lagern.</p>
    <p class="info-strip__fact"><strong>Ursprungsland:</strong>Deutschland</p>
    <div class="info-strip__lot"></div>
    <p class="info-strip__weight">500g</p>
    <div class="info-strip__rule"></div>
    <address class="info-strip__address"><strong>Imkerei Brenntal</strong><br>Auenweg 12<br>85399 Kleinfeld<br>info@imkerei-brenntal.de</address>
  </div>
  <div class="front-band">
    <div class="front-band__pattern" role="img" aria-label="Grafische Pusteblumen-Samenstände auf Blau"></div>
    <div class="name-plate"><div class="name-plate__frame">
      <div class="name-plate__mark"></div>
      <p class="name-plate__region">BAYERISCHER</p>
      <h2 class="name-plate__title">BIENENHONIG</h2>
      <p class="name-plate__season">Frühtracht</p>
      <p class="name-plate__kind">Blütenhonig cremig gerührt</p>
    </div></div>
  </div>
</section>

<section class="label-set label-set--spaet">
  <div class="info-strip">
    <div class="info-strip__mark"></div>
    <p class="info-strip__note">Bienenhonig kristallisiert bei längerer Lagerung. Durch Erwärmen im Wasserbad bei 40° C kann Honig ohne Schaden wieder verflüssigt werden.</p>
    <p class="info-strip__fact"><strong>Lagerhinweis:</strong>Kühl, dunkel und trocken lagern.</p>
    <p class="info-strip__fact"><strong>Ursprungsland:</strong>Deutschland</p>
    <div class="info-strip__lot"></div>
    <p class="info-strip__weight">500g</p>
    <div class="info-strip__rule"></div>
    <address class="info-strip__address"><strong>Imkerei Brenntal</strong><br>Auenweg 12<br>85399 Kleinfeld<br>info@imkerei-brenntal.de</address>
  </div>
  <div class="front-band">
    <div class="front-band__pattern" role="img" aria-label="Geäderte Laubblätter in dunklem Grün"></div>
    <div class="name-plate"><div class="name-plate__frame">
      <div class="name-plate__mark"></div>
      <p class="name-plate__region">BAYERISCHER</p>
      <h2 class="name-plate__title">BIENENHONIG</h2>
      <p class="name-plate__season">Spättracht</p>
      <p class="name-plate__kind">Waldhonig</p>
    </div></div>
  </div>
</section>

</body>
</html>
```